Chairside Roots: the dental helper's field guide, start to finish

Book cover:

Book about dental implantology
Reader is a dental assistant
Introduction to surgical knowledge to case acceptance. We will start with the intro to implants that will cover population stats on tooth loss, how to make the patient trust the team, how to communicate with the patient. Then we will get more technical; bone loss, bone quality and quantity. We will also inform on pros and cons of different classic dental treatments vs implant treatment. Surgical knowledge deep into various aspects of implants procedures. An illustration of surgical instruments needed and motors and hand pieces. Operatory set up will be demonstrated. I’ll be guiding the role of the surgical assistant and non surgical assistant. At the end I’ll explain how to close an implant case. From single implants to more complex cases.

Target Market(s)

Dental assistants

Industry/Entity Type

Dental

Font styles to use
Other font styles liked:
• Mellifluous or addington

Colors
EE7325
F08F49
F5BC92
FAE3D3
FDF4ED

Requirements
Must have
• Dental implant, positive vibe, orange Colors, professional
Nice to have
• Sense of team spirit, uncluttered,
Should not have
• Images of people

```html
<!DOCTYPE html>
<html lang="en">
<head>
<meta charset="UTF-8">
<title>Chairside Roots – Book Cover</title>
<link rel="stylesheet" href="https://fonts.googleapis.com/css2?family=Anton&family=Montserrat:wght@500;600&family=Chicle&display=swap">
<style>
  :root {
    --ink: #0a0a0a;
    --paper: #ffffff;
    --orange-deep: #ee7325;
    --orange-mid: #f08f49;
    --blob-light: #fb9b3a;
    --blob-strong: #fb7d0a;
    --amber: #f5a524;
    --glow: #fdd060;
    --band: #f9922a;
    --crown-white: #f4f4f4;
    --metal-grey: #a6a6a6;
  }
  * { margin: 0; padding: 0; box-sizing: border-box; }
  html, body { width: 850px; height: 1200px; overflow: hidden; background: var(--paper); }

  .cover {
    position: relative;
    width: 850px;
    height: 1200px;
    overflow: hidden;
    background: var(--paper);
  }

  .title-block {
    position: absolute;
    top: 0; left: 0;
    width: 850px;
    height: 480px;
    text-align: center;
  }
  .title-main {
    position: absolute;
    left: 0; right: 0;
    font-family: "Anton", "Bebas Neue", sans-serif;
    font-weight: 400;
    color: var(--ink);
    line-height: 1;
    font-size: 136px;
    letter-spacing: 1px;
  }
  .title-main--top { top: 88px; }
  .title-main--bottom { top: 208px; }

  .subtitle {
    position: absolute;
    top: 352px; left: 0; right: 0;
    font-family: "Montserrat", sans-serif;
    font-weight: 600;
    font-size: 27px;
    line-height: 1;
    letter-spacing: 3px;
    color: var(--ink);
  }

  .range-pill {
    position: absolute;
    top: 402px; left: 311px;
    width: 228px; height: 51px;
    border: 1.5px solid #333;
    border-radius: 26px;
    display: flex;
    align-items: center;
    justify-content: center;
    gap: 10px;
    font-family: "Montserrat", sans-serif;
    font-weight: 500;
    font-size: 21px;
    color: var(--ink);
  }
  .range-pill svg { display: block; }

  .art-panel {
    position: absolute;
    top: 480px; left: 0;
    width: 850px; height: 720px;
    background:
      radial-gradient(ellipse 60% 45% at 40% 20%, var(--glow) 0%, rgba(253,208,96,0) 70%),
      linear-gradient(180deg, var(--amber) 0%, #f29a1c 60%, #f08e14 78%, #fbbf48 88%, #f39419 100%);
  }
  .art-panel::before {
    content: "";
    position: absolute;
    top: 0; left: 0; right: 0;
    height: 4px;
    background: var(--band);
  }

  .art-shapes {
    position: absolute;
    top: 0; left: 0;
  }

  .implant-visual {
    position: absolute;
    left: 294px; top: 543px;
    width: 241px; height: 507px;
    border-radius: 28px;
    background: linear-gradient(180deg, var(--crown-white) 0%, #e2e2e2 45%, var(--metal-grey) 100%);
  }

  .bubble-label {
    position: absolute;
    font-family: "Chicle", "Chewy", cursive;
    color: var(--ink);
    font-size: 27px;
    line-height: 0.95;
  }
  .bubble-label--efficiency { left: 243px; top: 636px; }
  .bubble-label--matters { left: 565px; top: 722px; }
  .bubble-label--takes { left: 217px; top: 868px; }
  .bubble-label--team { left: 494px; top: 930px; }

  .author-name {
    position: absolute;
    top: 1097px; left: 0; right: 0;
    text-align: center;
    font-family: "Montserrat", sans-serif;
    font-weight: 500;
    font-size: 22px;
    letter-spacing: 19px;
    padding-left: 19px;
    color: var(--ink);
  }
</style>
</head>
<body>
  <main class="cover">
    <header class="title-block">
      <h1>
        <span class="title-main title-main--top">CHAIRSIDE</span>
        <span class="title-main title-main--bottom">ROOTS</span>
      </h1>
      <p class="subtitle">THE DENTAL HELPER'S FIELD GUIDE</p>
      <div class="range-pill">
        <span>start</span>
        <svg width="50" height="10" viewBox="0 0 50 10" aria-hidden="true">
          <line x1="0" y1="5" x2="44" y2="5" stroke="#0a0a0a" stroke-width="1.2"/>
          <polygon points="44,2 50,5 44,8" fill="#0a0a0a"/>
        </svg>
        <span>finish</span>
      </div>
    </header>

    <section class="art-panel"></section>

    <svg class="art-shapes" width="850" height="1200" viewBox="0 0 850 1200" aria-hidden="true">
      <circle class="orbit-ring" cx="422" cy="816" r="178" fill="none" stroke="#ffffff" stroke-width="1.3"/>
    </svg>

    <div class="implant-visual" role="img" aria-label="Illustration of a dental implant: white molar crown on a threaded titanium screw"></div>

    <svg class="art-shapes" width="850" height="1200" viewBox="0 0 850 1200" aria-hidden="true">
      <path class="bubble bubble--efficiency" fill="#fb9b3a"
        d="M262 598 C300 590 330 608 355 628 C380 650 380 680 365 700 C345 722 310 733 285 733 C255 733 240 710 228 680 C215 648 215 618 262 598 Z"/>
      <path class="bubble bubble--matters" fill="#fb9b3a"
        d="M585 695 C615 685 640 678 655 680 C672 684 678 700 680 730 C682 768 670 796 640 802 C605 806 560 797 540 778 C515 755 525 715 585 695 Z"/>
      <path class="bubble bubble--takes" fill="#fb7d0a"
        d="M260 830 C290 828 312 840 315 868 C318 895 305 925 287 943 C270 958 240 953 210 942 C180 930 170 905 176 885 C186 855 225 832 260 830 Z"/>
      <path class="bubble bubble--team" fill="#fb7d0a"
        d="M520 901 C545 898 565 908 585 926 C610 948 622 965 616 990 C608 1015 570 1033 530 1035 C498 1036 480 1010 470 985 C460 955 470 905 520 901 Z"/>
    </svg>

    <p class="bubble-label bubble-label--efficiency">the way<br>to efficiency</p>
    <p class="bubble-label bubble-label--matters">what<br>matters</p>
    <p class="bubble-label bubble-label--takes">what it<br>takes</p>
    <p class="bubble-label bubble-label--team">benefiting<br>the entire<br>team</p>

    <p class="author-name">AUTHOR'S NAME</p>
  </main>
</body>
</html>
```